LumoPledge Crowdfunding Website 1st Page

I am looking to have a first page created for a new crowd funding website that knocks down the biggest hurdle that creative types and start ups face, legal costs. For creative projects and innovative products, we are providing intellectual property and certain other legal services wrapped into the project costs.

I am using a white label crowdfunding platform that that has a standard look and feel of most crowdfunding sites e.g. tiles with campaigns, listing of campaigns categories, create new campaign options, and donate to campaigns etc. The white label program is branded with the LumoPledge logo and colors. At present there is a front page that is just a place holder for someone at ArtHively's great design! What I need is an eye-catching first page that visually and through content optimizes the LumoPledge brand. (There should be space for content for those looking to raise money and those looking to donate to campaigns.)

www.fundvexora.com is, of course, the reigning King of crowdfunding. They have been so successful that they no longer have to entice people to launch campaigns there. (So they don't speak as much to those looking to raise money.) Unlike Fundvexora, of the challenges is that I have two customers I need to engage. The first is the potential crowdfund campaign owner who is looking to raise money. The second customer is the donor.

I am looking for a smart page from a marketing standpoint that also grabs you. One should feel the energy of "the crowd" when they look at the page.

Some information regarding the logo: The font is Kabel BK BT. The primary blue is R33, G121, B 159. Hex21799F and the primary greenis R179, G210, B54 Hex B3D236. The third file is a slight variation on the LP logo that you are free to use as well. (Unfortunately, I don't have all the color information for that one readily available.) If you need more files, please just let me know.

Industry/Entity Type

Marketing

Font styles to use
Other font styles liked:
• Kabel Bk BT or complimentary

Requirements
Must have
• Please use the slogan "Where the crowd meets great ideas".

```html
<!DOCTYPE html>
<html lang="en">
<head>
<meta charset="utf-8">
<title>LumoPledge – Where the crowd meets great ideas</title>
<link href="https://fonts.googleapis.com/css2?family=Didact+Gothic&family=Open+Sans:wght@400;600;700&display=swap" rel="stylesheet">
<style>
  :root {
    --brand-ink: #2f3a44;
    --hero-blue: #1cb3dd;
    --hero-blue-dark: #119fcb;
    --ink: #333b44;
    --ink-soft: #6a6f75;
    --button: #323c47;
    --button-edge: #1c232b;
    --accent-green: #7fb51e;
    --bar-green: #5cb85c;
    --bar-red: #d9534f;
    --bar-track: #ececec;
    --page: #ffffff;
    --band: #f6f6f6;
    --line: #e3e3e3;
  }
  * { box-sizing: border-box; margin: 0; padding: 0; }
  html, body { width: 1200px; height: 1069px; overflow: hidden; }
  body { background: var(--page); font-family: "Open Sans", Arial, sans-serif; color: var(--ink); position: relative; }

  .site-header { position: absolute; left: 0; top: 0; width: 1200px; height: 113px; background: #fbfbfb; }
  .brand { position: absolute; left: 128px; top: 58px; font-family: "Didact Gothic", Arial, sans-serif;
           font-size: 28px; line-height: 34px; color: var(--brand-ink); white-space: nowrap; }
  .search { position: absolute; left: 861px; top: 15px; width: 211px; height: 28px; border: 1px solid #e2e2e2;
            border-radius: 14px; background: #fff; font-size: 11px; color: #777; padding: 6px 0 0 14px; }
  .search svg { position: absolute; right: 12px; top: 8px; }
  .main-nav { position: absolute; top: 69px; left: 0; font-size: 12px; font-weight: 700; color: #3a3a3a; }
  .main-nav span { position: absolute; white-space: nowrap; }
  .main-nav .login { color: #23a4d1; }

  .hero { position: absolute; left: 0; top: 113px; width: 1200px; height: 395px;
          background: linear-gradient(180deg, var(--hero-blue) 0%, var(--hero-blue-dark) 100%); color: #fff; text-align: center; }
  .hero-title { position: absolute; top: 52px; width: 100%; font-family: "Didact Gothic", Arial, sans-serif; font-size: 37px; font-weight: 400; }
  .hero-rule { position: absolute; left: 257px; top: 122px; width: 683px; height: 5px; border-top: 1px solid #fff; border-bottom: 1px solid #fff; opacity: .85; }
  .hero-col { position: absolute; width: 420px; }
  .hero-col h2 { font-family: "Didact Gothic", Arial, sans-serif; font-weight: 400; font-size: 24px; line-height: 30px; white-space: nowrap; }
  .hero-col p { font-size: 12.5px; line-height: 19px; margin-top: 18px; white-space: nowrap; }
  .btn { position: absolute; height: 43px; background: var(--button); border-bottom: 4px solid var(--button-edge);
         color: #fff; font-family: "Didact Gothic", Arial, sans-serif; font-size: 20px; line-height: 39px; text-align: center; }

  .section-title { position: absolute; left: 128px; top: 528px; font-family: "Didact Gothic", Arial, sans-serif; font-size: 20px; color: #555; font-weight: 400; }
  .slider-arrow { position: absolute; top: 675px; }
  .card { position: absolute; top: 576px; width: 228px; height: 252px; background: #fff; box-shadow: 0 0 4px rgba(0,0,0,.12); }
  .card-media { position: relative; height: 114px; }
  .price { position: absolute; left: 0; bottom: 0; width: 100%; height: 23px; background: rgba(40,40,40,.6);
           color: #fff; font-size: 19px; line-height: 23px; padding-left: 14px; }
  .card-body { padding: 4px 12px 0; }
  .card-name { color: var(--accent-green); font-weight: 700; font-size: 12.5px; }
  .card-desc { color: var(--ink-soft); font-size: 12px; line-height: 15px; margin-top: 2px; padding-bottom: 8px; border-bottom: 1px solid var(--line); }
  .progress { margin-top: 10px; height: 10px; border-radius: 5px; background: var(--bar-track); overflow: hidden; }
  .progress i { display: block; height: 100%; border-radius: 5px; }
  .stats { display: flex; justify-content: space-between; margin-top: 12px; font-size: 12px; color: #555; white-space: nowrap; }
  .stats b { display: block; font-weight: 400; color: var(--accent-green); margin-top: 2px; }

  .browse-band { position: absolute; left: 0; top: 879px; width: 1200px; height: 190px; background: var(--band); }
  .filter-tabs { position: absolute; left: 330px; top: 903px; width: 554px; height: 41px; border-radius: 20px;
                 background: #ececec; box-shadow: 0 2px 3px rgba(0,0,0,.15); display: flex; align-items: center;
                 justify-content: space-between; padding: 0 14px; font-size: 12.5px; color: #444; }
  .filter-tabs span { display: flex; align-items: center; gap: 8px; padding: 0 18px; border-right: 1px solid #d8d8d8;
                      height: 24px; white-space: nowrap; }
  .filter-tabs span:last-child { border-right: 0; }
  .categories { position: absolute; left: 128px; top: 990px; width: 182px; list-style: none; font-family: "Didact Gothic", Arial, sans-serif; font-size: 17px; color: #333; }
  .categories li { height: 37px; padding-top: 6px; border-bottom: 1px dotted #aaa; }
  .grid-tile { position: absolute; top: 980px; width: 228px; height: 89px; }
</style>
</head>
<body>
  <header class="site-header">
    <div class="brand">LumoPledge</div>
    <div class="search">Enter keyword here
      <svg width="11" height="11" viewBox="0 0 11 11"><circle cx="4.5" cy="4.5" r="3.5" fill="none" stroke="#999" stroke-width="1.5"/><line x1="7" y1="7" x2="10" y2="10" stroke="#999" stroke-width="1.5"/></svg>
    </div>
    <nav class="main-nav">
      <span style="left:540px">HOW IT WORKS</span>
      <span style="left:695px">DISCOVER</span>
      <span style="left:818px">START A PROJECT</span>
      <span class="login" style="left:973px">LOGIN / SIGN UP</span>
    </nav>
  </header>

  <section class="hero" role="img" aria-label="Faint city skyline photo tinted blue behind the hero text">
    <h1 class="hero-title">Where the crowd meets great ideas !</h1>
    <div class="hero-rule"></div>
    <div class="hero-col" style="left:135px;top:170px">
      <h2>Discover Amazing projects or<br>Start your own for Free</h2>
      <p>Lorem Ipsum is simply dummy text of the printing and typesetting<br>industry. Lorem Ipsum has been the industry's standard dummy<br>text ever since the 1500s,</p>
    </div>
    <a class="btn" style="left:264px;top:327px;width:148px">Start now</a>
    <div class="hero-col" style="left:632px;top:193px">
      <h2>Find projects that interest you,</h2>
      <p>Lorem Ipsum is simply dummy text of the printing and typesetting<br>industry. Lorem Ipsum has been the industry's standard dummy<br>text ever since the 1500s,</p>
    </div>
    <a class="btn" style="left:777px;top:325px;width:163px">Browse now</a>
  </section>

  <h3 class="section-title">Populor Projects</h3>
  <svg class="slider-arrow" style="left:70px" width="16" height="26" viewBox="0 0 16 26"><polyline points="14,2 3,13 14,24" fill="none" stroke="#fff" stroke-width="3"/><polyline points="14,2 3,13 14,24" fill="none" stroke="#ccc" stroke-width="1"/></svg>
  <svg class="slider-arrow" style="left:1110px" width="16" height="26" viewBox="0 0 16 26"><polyline points="2,2 13,13 2,24" fill="none" stroke="#fff" stroke-width="3"/><polyline points="2,2 13,13 2,24" fill="none" stroke="#ccc" stroke-width="1"/></svg>

  <article class="card" style="left:128px">
    <div class="card-media" role="img" aria-label="Photo of a band posing in front of a stage curtain" style="background:linear-gradient(135deg,#6b4a35,#8a3b2c 50%,#4b5b62)"><div class="price">$ 9450</div></div>
    <div class="card-body">
      <div class="card-name">Project Name</div>
      <div class="card-desc">It was popularised in the 1960s with the release of Letraset sheets.</div>
      <div class="progress"><i style="width:50%;background:var(--bar-green)"></i></div>
      <div class="stats"><div>Funded<b>50%</b></div><div>owner<b>Jonny Reed</b></div><div>Days left<b>20</b></div></div>
    </div>
  </article>

  <article class="card" style="left:367px">
    <div class="card-media" role="img" aria-label="Photo of an open illustrated children's book" style="background:linear-gradient(135deg,#c79a9e,#d8c8c0 55%,#e9e7e2)"><div class="price">$ 650</div></div>
    <div class="card-body">
      <div class="card-name">Project Name</div>
      <div class="card-desc">It was popularised in the 1960s with the release of Letraset sheets.</div>
      <div class="progress"><i style="width:22%;background:var(--bar-green)"></i></div>
      <div class="stats"><div>Funded<b>50%</b></div><div>owner<b>Jonny Reed</b></div><div>Days left<b>10</b></div></div>
    </div>
  </article>

  <article class="card" style="left:607px">
    <div class="card-media" role="img" aria-label="Photo of farmers standing in a golden field" style="background:linear-gradient(180deg,#7c8d4e,#b88a3a 55%,#c9992f)"><div class="price">$ 3230</div></div>
    <div class="card-body">
      <div class="card-name">Project Name</div>
      <div class="card-desc">It was popularised in the 1960s with the release of Letraset sheets.</div>
      <div class="progress"><i style="width:76%;background:var(--bar-red)"></i></div>
      <div class="stats"><div>Funded<b>50%</b></div><div>owner<b>Jonny Reed</b></div><div>Days left<b>1</b></div></div>
    </div>
  </article>

  <article class="card" style="left:846px">
    <div class="card-media" role="img" aria-label="Blue ink comic sketch on grid paper" style="background:linear-gradient(135deg,#f2f2f6,#d9d8ea 60%,#eeeef3)"><div class="price">$ 2250</div></div>
    <div class="card-body">
      <div class="card-name">Project Name</div>
      <div class="card-desc">It was popularised in the 1960s with the release of Letraset sheets.</div>
      <div class="progress"><i style="width:50%;background:var(--bar-green)"></i></div>
      <div class="stats"><div>Funded<b>50%</b></div><div>owner<b>Jonny Reed</b></div><div>Days left<b>35</b></div></div>
    </div>
  </article>

  <section class="browse-band"></section>
  <nav class="filter-tabs">
    <span><svg width="15" height="14" viewBox="0 0 15 14"><path d="M7.5 1C3.9 1 1 3.3 1 6.2c0 1.5.8 2.8 2 3.8L2.5 13l3.3-1.8c.6.1 1.1.2 1.7.2 3.6 0 6.5-2.3 6.5-5.2S11.1 1 7.5 1z" fill="none" stroke="#333" stroke-width="1.5"/></svg>Most Populor</span>
    <span><svg width="11" height="15" viewBox="0 0 11 15"><path d="M5.5 0C2.5 0 0 2.4 0 5.4 0 9.5 5.5 15 5.5 15S11 9.5 11 5.4C11 2.4 8.5 0 5.5 0z" fill="#333"/><circle cx="5.5" cy="5.3" r="2" fill="#ececec"/></svg>Near Me</span>
    <span><svg width="14" height="13" viewBox="0 0 14 13"><path d="M1 4h10M8 1l3 3-3 3M13 9H3M6 6l-3 3 3 3" fill="none" stroke="#333" stroke-width="2"/></svg>Live Feed</span>
    <span><svg width="12" height="13" viewBox="0 0 12 13"><circle cx="6" cy="3.5" r="3" fill="#333"/><path d="M0 13c0-4 2.7-6 6-6s6 2 6 6z" fill="#333"/></svg>Funded Buy Friends</span>
  </nav>
  <ul class="categories">
    <li>Art</li>
    <li>Comics</li>
  </ul>
  <div class="grid-tile" style="left:348px;background:linear-gradient(135deg,#6b4a35,#8a3b2c 50%,#4b5b62)" role="img" aria-label="Photo of a band posing in front of a stage curtain"></div>
  <div class="grid-tile" style="left:595px;background:linear-gradient(135deg,#c79a9e,#d8c8c0 55%,#e9e7e2)" role="img" aria-label="Photo of an open illustrated children's book"></div>
  <div class="grid-tile" style="left:843px;background:linear-gradient(180deg,#7c8d4e,#b88a3a 55%,#c9992f)" role="img" aria-label="Photo of farmers standing in a golden field"></div>
</body>
</html>
```